Design some Business Cards for Birch Meadow

could someone please design some snazzy business cards for "Birch Meadow"
the website is birchmeadow.co.nz

the logo is attached

name : Harriet Doucan
Contact Number: 0224819357
email: harrietdouc@birchmeadow.co.nz
Slogan: Competitive prices, and personal service in the Wanganui district

The theme is green as its for a lawn mowing outfit!

```html
<!DOCTYPE html>
<html lang="en">
<head>
<meta charset="utf-8">
<title>Birch Meadow — Business Cards</title>
<link rel="stylesheet" href="https://fonts.googleapis.com/css2?family=Arimo:wght@400;700&display=swap">
<style>
  :root {
    --backdrop: #e8e5df;
    --card: #ffffff;
    --green: #66793d;
    --green-dark: #53652c;
    --green-pale: #e3e9d6;
    --ink: #4f6228;
  }
  * { margin: 0; padding: 0; box-sizing: border-box; }
  html, body { width: 1200px; height: 899px; overflow: hidden; background: var(--backdrop); }
  .canvas { position: relative; width: 1200px; height: 899px; font-family: "Arimo", Arial, sans-serif; color: var(--ink); }
  .card {
    position: absolute; left: 328px; width: 582px; height: 322px;
    background: var(--card); overflow: hidden;
    box-shadow: 0 3px 10px rgba(0,0,0,0.18);
  }
  .card--front { top: 91px; }
  .card--back { top: 440px; }
  .edge-band { position: absolute; top: 0; bottom: 0; }
  .edge-band--left { left: 0; background: linear-gradient(90deg, var(--green), rgba(102,121,61,0)); }
  .edge-band--right { right: 0; background: linear-gradient(270deg, var(--green), rgba(102,121,61,0)); }
  .card--front .edge-band--left { width: 26px; }
  .card--front .edge-band--right { width: 40px; }
  .card--back .edge-band--left { width: 44px; }
  .card--back .edge-band--right { width: 30px; }
  .brand-mark {
    position: absolute; left: 0; right: 0; top: 96px;
    display: flex; flex-direction: column; align-items: center; gap: 18px;
  }
  .brand-mark__dot { width: 46px; height: 46px; border-radius: 50%; background: var(--green); }
  .brand-mark__name { font-size: 36px; font-weight: 700; color: var(--green-dark); letter-spacing: 1px; }
  .front-slogan {
    position: absolute; left: 40px; right: 44px; top: 296px; text-align: center;
    font-size: 12.5px; letter-spacing: 1.3px; word-spacing: 3px; color: var(--ink); white-space: nowrap;
  }
  .back-brand {
    position: absolute; left: 0; right: 0; top: 22px; text-align: center;
    font-size: 14px; font-weight: 700; color: var(--green-dark);
  }
  .name-band {
    position: absolute; left: 137px; top: 100px; width: 290px; height: 36px;
    background: var(--green-pale);
    display: flex; align-items: center; justify-content: center;
  }
  .name-band__name { font-size: 23px; letter-spacing: 2.5px; color: var(--green-dark); }
  .back-slogan {
    position: absolute; left: 0; right: 0; top: 175px; text-align: center;
    font-size: 20px; line-height: 30px; letter-spacing: 1.4px; word-spacing: 4px; color: var(--ink);
  }
  .contact {
    position: absolute; left: 0; right: 0; top: 272px;
    display: flex; flex-direction: column; align-items: center; gap: 4px;
    font-size: 15px; letter-spacing: 0.6px; color: var(--green-dark);
  }
  .contact__line { display: flex; align-items: center; gap: 6px; }
  .contact__icon { width: 14px; height: 14px; }
</style>
</head>
<body>
<main class="canvas">

  <section class="card card--front" aria-label="Card front">
    <div class="edge-band edge-band--left" role="img" aria-label="Green edge decoration"></div>
    <div class="edge-band edge-band--right" role="img" aria-label="Green edge decoration"></div>
    <div class="brand-mark">
      <span class="brand-mark__dot"></span>
      <span class="brand-mark__name">Birch Meadow</span>
    </div>
    <p class="front-slogan">Competitive prices, and personal service in the Wanganui district</p>
  </section>

  <section class="card card--back" aria-label="Card back">
    <div class="edge-band edge-band--left" role="img" aria-label="Green edge decoration"></div>
    <div class="edge-band edge-band--right" role="img" aria-label="Green edge decoration"></div>
    <p class="back-brand">Birch Meadow</p>
    <div class="name-band"><span class="name-band__name">Harriet Doucan</span></div>
    <p class="back-slogan">Competitive prices, and personal service<br>in the Wanganui district</p>
    <div class="contact">
      <p class="contact__line">
        <svg class="contact__icon" viewBox="0 0 14 14" aria-hidden="true"><rect width="14" height="14" rx="2" fill="#53652c"/><path d="M4 3 Q3 7 6 10 Q8 11.5 10 11 L10 9 L8.5 8.5 L7.6 9.3 Q5.5 8 4.8 5.6 L5.6 4.8 L5.2 3 Z" fill="#fff"/></svg>
        0224819357
      </p>
      <p class="contact__line">
        <svg class="contact__icon" viewBox="0 0 14 14" aria-hidden="true"><rect width="14" height="14" rx="2" fill="#53652c"/><path d="M2.5 4 H11.5 V10.5 H2.5 Z M2.5 4 L7 7.8 L11.5 4" fill="none" stroke="#fff" stroke-width="1.1"/></svg>
        harrietdouc@birchmeadow.co.nz
      </p>
    </div>
  </section>

</main>
</body>
</html>
```